New Packaging Design Project

Wine packaging redesign. Retail partner requested a redesign of a private label wine. The old label is attached. Our partner liked the Copper Wren Hollow label and wanted something similar. There will be a logo added to the top of the label

Went on vacation/holiday

```html
<!DOCTYPE html>
<html lang="en">
<head>
<meta charset="utf-8">
<title>Napa Valley Red Blend Label</title>
<link href="https://fonts.googleapis.com/css2?family=Cinzel:wght@400;500&family=Cormorant+Garamond:wght@500&display=swap" rel="stylesheet">
<style>
  :root {
    --backdrop: #2b2929;
    --label-black: #0d0d0d;
    --gold: #b48c52;
    --fine-text: #bdb8b0;
    --art-light: #8f8b86;
    --art-dark: #3a3836;
  }
  * { margin: 0; padding: 0; box-sizing: border-box; }
  html, body {
    width: 734px;
    height: 1200px;
    overflow: hidden;
    background: var(--backdrop);
  }
  .canvas {
    position: relative;
    width: 734px;
    height: 1200px;
  }
  .label {
    position: absolute;
    left: 47px;
    top: 191px;
    width: 640px;
    height: 817px;
    background: var(--label-black);
  }
  .region {
    position: absolute;
    top: 128px;
    width: 100%;
    text-align: center;
    font-family: "Cinzel", serif;
    font-weight: 500;
    font-size: 58px;
    letter-spacing: 1px;
    color: var(--gold);
  }
  .vineyard-art {
    position: absolute;
    left: 93px;
    top: 234px;
    width: 454px;
    height: 272px;
    background: linear-gradient(160deg, var(--art-light) 0%, var(--art-dark) 55%, var(--art-light) 100%);
  }
  .wine-name {
    position: absolute;
    top: 535px;
    width: 100%;
    text-align: center;
    font-family: "Cinzel", serif;
    font-size: 36px;
    letter-spacing: 3px;
    color: var(--gold);
  }
  .varietals {
    position: absolute;
    left: 302px;
    top: 594px;
    list-style: none;
    font-family: "Cinzel", serif;
    font-size: 12px;
    line-height: 21px;
    letter-spacing: 0.5px;
    color: var(--fine-text);
  }
  .vintage {
    position: absolute;
    top: 700px;
    width: 100%;
    text-align: center;
    font-family: "Cormorant Garamond", serif;
    font-weight: 500;
    font-size: 40px;
    color: var(--gold);
  }
</style>
</head>
<body>
  <main class="canvas">
    <section class="label">
      <h1 class="region">NAPA VALLEY</h1>
      <div class="vineyard-art" role="img" aria-label="Line illustration of rolling vineyard rows in light grey on black"></div>
      <h2 class="wine-name">RED BLEND</h2>
      <ul class="varietals">
        <li>MERLOT</li>
        <li>CABERNET SAUVIGNON</li>
        <li>CABERNET FRANC</li>
        <li>PETIT VERDOT</li>
        <li>MALBEC</li>
      </ul>
      <p class="vintage">2018</p>
    </section>
  </main>
</body>
</html>
```